The Harbor and Lantern: for Lucille and Desmond by Odessa Varrow

I need an album cover design for a song dedicated to Desmond and Lucille Ames Bellamy, in anticipation for DAB weekend. the main question the song raises is: when was the last time someone said that you can achieve greatness? In other words, we often do not live to our full potential. The design should be simple and clean, using a modern Sans Serif font. 1600 x 1600 pixels, best-quality RGB mode, and delivered as a JPEG.

Target Market(s)

young men and women, 18-35 years old

Font styles to use
Sans Serif

Colors
3277b5
34a7d7

Requirements
Must have
• Name of song (The Harbor and Lantern: for Lucille and Desmond) and artist (Odessa Varrow)
Nice to have
• Something suggesting elegance without being overt or pretentious
Should not have
• Serif font, too many colors

```html
<!DOCTYPE html>
<html lang="en">
<head>
<meta charset="utf-8">
<title>The Harbor and Lantern — Odessa Varrow</title>
<link rel="stylesheet" href="https://fonts.googleapis.com/css2?family=Belleza&family=Great+Vibes&display=swap">
<style>
  :root {
    --cover-blue: #0096d6;
    --cover-blue-light: #12a3de;
    --cover-blue-deep: #0090cf;
    --emblem-dark: #3277b5;
    --emblem-light: #34a7d7;
    --ink-white: #ffffff;
  }
  html, body {
    margin: 0;
    padding: 0;
    width: 1200px;
    height: 1200px;
    overflow: hidden;
  }
  .album-cover {
    position: relative;
    width: 1200px;
    height: 1200px;
    background: radial-gradient(circle at 50% 40%, var(--cover-blue-light) 0%, var(--cover-blue) 45%, var(--cover-blue-deep) 100%);
    color: var(--ink-white);
    overflow: hidden;
  }
  .emblem {
    position: absolute;
    left: 524px;
    top: 177px;
    width: 313px;
    height: 425px;
    border-radius: 18px;
    background: linear-gradient(160deg, var(--emblem-light) 0%, var(--emblem-dark) 100%);
  }
  .emblem-shadow {
    position: absolute;
    left: 500px;
    top: 596px;
    width: 260px;
    height: 16px;
    border-radius: 50%;
    background: radial-gradient(ellipse at center, rgba(0, 70, 120, 0.35) 0%, rgba(0, 70, 120, 0) 70%);
  }
  .song-title {
    position: absolute;
    left: 0;
    right: 0;
    top: 648px;
    margin: 0;
    text-align: center;
    font-family: "Belleza", sans-serif;
    font-weight: 400;
    font-size: 57px;
    line-height: 1;
    letter-spacing: 0.5px;
  }
  .dedication {
    position: absolute;
    left: 0;
    right: 0;
    top: 726px;
    margin: 0;
    text-align: center;
    font-family: "Belleza", sans-serif;
    font-size: 37px;
    line-height: 1;
    letter-spacing: 0.5px;
  }
  .artist-name {
    position: absolute;
    left: 0;
    right: 0;
    top: 1020px;
    margin: 0;
    text-align: center;
    font-family: "Great Vibes", cursive;
    font-size: 66px;
    line-height: 1;
    padding-left: 30px;
  }
</style>
</head>
<body>
  <main class="album-cover">
    <div class="emblem-shadow"></div>
    <div class="emblem" role="img" aria-label="Illustration of a raised fist beside a musical note, drawn in white and deep blue"></div>
    <h1 class="song-title">The Harbor and Lantern</h1>
    <p class="dedication">for LUCILLE and DESMOND</p>
    <p class="artist-name">Odessa Varrow</p>
  </main>
</body>
</html>
```